Storevanta product design and upload for Coffee Shop

Coffee Shop, Store Front & Online - Storevanta theme

***Important*** Credentials to complete the gig will only be shared via Keyvora or a similar password share application. Please ensure you will be able to do this before proceeding.

Please advise if you have worked with any Storevanta theme in mercavo?

Job Description
Set up and customize all products to Mercavo for my Coffee Shop and customize to my colours and brand - using the current installed storevanta theme.

Hi there, I have a "Physical retail Cafe" I am looking for someone to upload the attached menu for me in the products section of my Mercavo store and make the store look and display awesome. Need expert who has a good understanding of the mercavo and storevanta system as I need a quick turn around.

Existing Old site - www.mugabrill.com.au
New mercavo site to be set up with storevanta theme - https://mugabrill.mymercavo.com/

Attached in these excel spreadsheets are the menus:
1.Muga Brill Insotre Menu - Muga Brill Online Shop Menu
2. Muga Brill Online Shop Menu

1. In Store Menu - where customers can only purchase the items in the store - however they will be able to view all items online. So a visually appealing display of products and ease of viewing of the menu is important.
Currently customers can order this menu here - http://applinkr.example/q72zkp using phone app, computer or any device and pick up only from store.

2. Online Shop Menu - They can purchase these items online and we can ship.

Examples provided below of how I would like the sites I like - and would like similar design using our products and items. Please feel free to use your expertise to solve and issues or improve.
Also I am happy to discuss any ideas or questions you have.

We do not have many images of our products at the moment so please free to use any of the images from below sites as a temporary pic - unless you can source some better original ones or have some ideas...

Please see all attachments for full details.

Target Market(s)

Coffee Shop - Retail Store Front & Online

Colors
fffefc
ffffff

Requirements
Must have
• Pleas read attached brief
Nice to have
• Experience using storevanta theme. Open to using another theme if designer can deisgn style I am looking for as per the examples in the brief.
Should not have
• As per the brieft

```html
<!DOCTYPE html>
<html lang="en">
<head>
<meta charset="utf-8">
<title>Muga Brill – Gourmet Coffee</title>
<link href="https://fonts.googleapis.com/css2?family=Oswald:wght@400;500&family=Roboto:wght@400&family=Montserrat:ital,wght@0,400;1,400&family=Ubuntu:wght@400&display=swap" rel="stylesheet">
<style>
:root{
  --red:#ed1c24;
  --lime:#b5d334;
  --lime-soft:rgba(170,205,40,.78);
  --nav-bg:#f2f7f3;
  --nav-text:#9bbf2a;
  --ink:#3a3a3a;
  --black:#000;
  --white:#fff;
  --grey:#555;
}
*{box-sizing:border-box;margin:0;padding:0}
html,body{width:1200px;height:854px;overflow:hidden;background:var(--white)}
body{position:relative;font-family:"Roboto",sans-serif}
.abs{position:absolute}
.promo-bar{left:0;top:0;width:1200px;height:34px;background:var(--red)}
.promo-text{left:163px;top:7px;font:400 15px "Oswald",sans-serif;color:var(--white)}
.flag-in{left:416px;top:10px;width:20px;height:13px;border:1px solid #fff}
.currency{left:1015px;top:9px;font:400 13px "Oswald",sans-serif;color:var(--white);display:flex;align-items:center;gap:5px}
.cart-icon{left:1098px;top:6px}
.cart-count{left:1114px;top:2px;width:15px;height:15px;border-radius:50%;background:var(--lime);color:#fff;font:400 9px "Roboto",sans-serif;text-align:center;line-height:15px}
.brand{left:553px;top:6px;width:94px;height:94px;border-radius:50%;border:3px solid var(--red);background:var(--white);display:flex;align-items:center;justify-content:center;font:500 17px "Oswald",sans-serif;color:var(--red)}
.contact{left:883px;top:38px;font-family:"Oswald",sans-serif;color:var(--grey);line-height:1.3}
.contact .q{font-size:16px}
.contact .phone{font-size:16px;color:var(--nav-text);display:flex;align-items:center;gap:4px}
.contact .hours{font-size:13px}
.main-nav{left:66px;top:104px;width:1066px;height:41px;background:var(--nav-bg);border-top:1px solid var(--lime);border-bottom:1px solid var(--lime)}
.nav-item{top:0;height:39px;border-left:1px solid var(--lime);color:var(--nav-text);font:400 15px "Roboto",sans-serif;display:flex;align-items:center;justify-content:center}
.nav-item.last{border-right:1px solid var(--lime)}
.nav-item.shop{border:1px solid var(--lime);box-shadow:inset 0 0 0 1px var(--lime)}
.account{left:843px;top:12px;font:400 12px "Roboto",sans-serif;color:var(--nav-text)}
.hero{left:67px;top:145px;width:1065px;height:399px;background:linear-gradient(100deg,#6a6a5a 0%,#8a3a30 30%,#c4312a 55%,#b33a30 75%,#8a8070 100%)}
.menu-panel{left:67px;top:145px;width:1065px;height:227px;background:var(--lime-soft)}
.tab{top:174px;height:31px;border:2px solid #fff;color:#fff;font:400 16px "Ubuntu",sans-serif;display:flex;align-items:center;justify-content:center}
.tab.active{background:#fff;color:#6f8f15}
.tab-pointer{left:222px;top:203px}
.cup{top:241px;width:54px;height:52px;border-radius:6px 6px 14px 14px;background:linear-gradient(#c9a27a 0 14%,#1b1b1b 14%)}
.cup-label{top:300px;width:120px;text-align:center;color:#fff;font:400 16px/23px "Ubuntu",sans-serif}
.headline{left:0;top:593px;width:1200px;text-align:center;font:500 38px "Oswald",sans-serif;color:var(--ink)}
.signup{left:71px;top:651px;width:1057px;height:194px;background:var(--black)}
.signup-lead{left:71px;top:686px;width:1057px;text-align:center;color:#fff;font:400 16px "Montserrat",sans-serif}
.field{top:725px;height:33px;background:#fff;border:1px solid #ccc;border-radius:2px;padding-left:9px;display:flex;align-items:center;color:#888;font:400 14px "Montserrat",sans-serif}
.cta{left:863px;top:725px;width:110px;height:33px;background:#e00;color:#fff;font:400 14px "Montserrat",sans-serif;display:flex;align-items:center;justify-content:center}
.privacy{left:71px;top:792px;width:1057px;text-align:center;color:#fff;font:italic 400 11px "Montserrat",sans-serif;letter-spacing:-.3px}
.foot-line{left:67px;top:850px;width:533px;height:2px;background:#ddd}
</style>
</head>
<body>
<div class="abs promo-bar"></div>
<div class="abs promo-text">Spend ¥6,440 JPY to Unlock Free Shipping India</div>
<svg class="abs flag-in" viewBox="0 0 20 13"><rect width="20" height="4.3" fill="#f93"/><rect y="4.3" width="20" height="4.4" fill="#fff"/><rect y="8.7" width="20" height="4.3" fill="#138808"/><circle cx="10" cy="6.5" r="1.6" fill="none" stroke="#000080" stroke-width=".6"/></svg>
<div class="abs currency"><svg width="20" height="14" viewBox="0 0 20 14"><rect width="20" height="14" fill="#fff"/><circle cx="10" cy="7" r="4" fill="#bc002d"/></svg>JPY<svg width="10" height="6" viewBox="0 0 10 6"><path d="M1 1l4 4 4-4" stroke="#fff" stroke-width="1.6" fill="none"/></svg></div>
<svg class="abs cart-icon" width="24" height="22" viewBox="0 0 24 22"><path d="M1 2h4l3 11h12l3-8H7" fill="#fff" stroke="#fff" stroke-width="2" stroke-linejoin="round"/><circle cx="9" cy="18" r="2" fill="#fff"/><circle cx="19" cy="18" r="2" fill="#fff"/></svg>
<div class="abs cart-count">0</div>

<div class="abs brand">Muga Brill</div>

<div class="abs contact">
  <div class="q">Got a Question? Call Us</div>
  <div class="phone"><svg width="14" height="14" viewBox="0 0 24 24"><path d="M6.6 10.8a15 15 0 0 0 6.6 6.6l2.2-2.2a1 1 0 0 1 1-.25 11.4 11.4 0 0 0 3.6.57 1 1 0 0 1 1 1V20a1 1 0 0 1-1 1A17 17 0 0 1 3 4a1 1 0 0 1 1-1h3.5a1 1 0 0 1 1 1c0 1.25.2 2.45.57 3.57a1 1 0 0 1-.25 1z" fill="#666"/></svg>0400 555 018</div>
  <div class="hours">Mon-Sat 5.30am-12pm Eastern</div>
</div>

<nav class="abs main-nav">
  <div class="abs nav-item" style="left:166px;width:96px">HOME</div>
  <div class="abs nav-item shop" style="left:263px;width:98px">SHOP&nbsp;&nbsp;<svg width="10" height="6" viewBox="0 0 10 6"><path d="M1 1l4 4 4-4" stroke="#9bbf2a" stroke-width="1.5" fill="none"/></svg></div>
  <div class="abs nav-item" style="left:362px;width:129px">SUBSCRIBE</div>
  <div class="abs nav-item" style="left:491px;width:105px">VISIT</div>
  <div class="abs nav-item last" style="left:596px;width:125px">LEARN</div>
  <div class="abs account">MY ACCOUNT &nbsp;|&nbsp; CART</div>
</nav>

<div class="abs hero" role="img" aria-label="Photo of the red drive-thru coffee container shop with a customer in a white convertible at the window"></div>
<div class="abs menu-panel"></div>

<div class="abs tab active" style="left:112px;width:156px">Gourmet Coffee</div>
<svg class="abs tab-pointer" width="24" height="20" viewBox="0 0 24 20"><path d="M0 0h24L12 18z" fill="#fff"/></svg>
<div class="abs tab" style="left:298px;width:110px">Breakfast</div>
<div class="abs tab" style="left:441px;width:156px">Chai Latte &amp; Tea</div>
<div class="abs tab" style="left:625px;width:123px">Iced Drinks</div>
<div class="abs tab" style="left:774px;width:114px">Beverages</div>
<div class="abs tab" style="left:906px;width:170px">Coffee Beans 1kg</div>

<div class="abs cup" style="left:124px" role="img" aria-label="Black mug of cappuccino"></div>
<div class="abs cup" style="left:245px" role="img" aria-label="Black mug of flat white latte"></div>
<div class="abs cup" style="left:366px" role="img" aria-label="Black mug of hot chocolate"></div>
<div class="abs cup" style="left:488px" role="img" aria-label="Black mug of long black"></div>
<div class="abs cup" style="left:638px" role="img" aria-label="Black mug of mocha"></div>
<div class="abs cup" style="left:758px" role="img" aria-label="Black mug of babyccino"></div>
<div class="abs cup" style="left:877px" role="img" aria-label="Black mug of macchiato"></div>
<div class="abs cup" style="left:997px" role="img" aria-label="Black mug of espresso"></div>

<div class="abs cup-label" style="left:97px">Cappuccino</div>
<div class="abs cup-label" style="left:227px;width:90px">Flat White Latte</div>
<div class="abs cup-label" style="left:343px;width:110px;top:298px">Hot Chocolate</div>
<div class="abs cup-label" style="left:480px;width:70px;top:298px;text-align:left">Long Black</div>
<div class="abs cup-label" style="left:612px;top:302px">Mocha</div>
<div class="abs cup-label" style="left:732px;top:302px">Babyccino</div>
<div class="abs cup-label" style="left:851px">Macchiato</div>
<div class="abs cup-label" style="left:971px;top:297px">Espresso</div>

<h1 class="abs headline">YOUR FREE COFFEE AWAITS...</h1>

<section class="abs signup"></section>
<p class="abs signup-lead">Enter your name and email address and you will be just one step away from your FREE COFFEE</p>
<div class="abs field" style="left:226px;width:202px">First Name</div>
<div class="abs field" style="left:437px;width:202px">Last Name</div>
<div class="abs field" style="left:648px;width:204px">Email</div>
<div class="abs cta">GET IT NOW</div>
<p class="abs privacy">We will not share your details with anyone else!</p>
<div class="abs foot-line"></div>
</body>
</html>
```